Trifold A4 doublesided flyer/brochure and possibly logo redisgn for Qorvel Vending solutions

We are a Sydney based drink and snack vending machine company that supply maintain and restock free vending machines for Sydney businesses. Most our sites are office work places as well as some training organizations and a gym. We require a Trifold A4 double sided flyer/brochure we can letterbox drop to local businesses that have a large amount of staff and would benefit from a vending machine in there staff lunchroom. We would also like to use the flyer for larger businesses that may have a showroom for there own customers.
The flyer needs to look sophisticated modern and professional and immediately convey the offer of a fully installed serviced and maintained vending machine absolutely FREE.
Also needs to include
Vending machine features
Our large range of products especially healthy options
Our ongoing support and servicing and commitment to superior service
We essentially dont have a logo so some sort of logo design would be a bonus
I am trying to look for high quality pictures suitable for print but i am finding it difficult.
I will keep searching and post soon.
We would like the original document or the general background as well so we can modify or add new text later our self resend a different version of the flyer
Our website has some pictures but they are not good enough for print.
www.qorvelindustries.com.au
We can use the main elements form the website but does not need to look the same or use the same fonts. you can give any thing a try although it would be good to tie in

Requirements
Must have
• I have uploaded a word document with some content and some pictures.
Pictures can be used at your discretion. you dont have to use these

```html
<!DOCTYPE html>
<html lang="en">
<head>
<meta charset="utf-8">
<title>Qorvel Vending solutions – Services Panel</title>
<link href="https://fonts.googleapis.com/css2?family=Archivo+Black&family=Arimo:wght@400&display=swap" rel="stylesheet">
<style>
  :root {
    --page: #ffffff;
    --sky: #8bc6d8;
    --leaf: #55bb5f;
    --ink: #1b1b1b;
    --paper-text: #ffffff;
    --photo-dark: #2a2f33;
    --photo-mid: #6d7a80;
    --photo-light: #c9d3d6;
  }
  * { box-sizing: border-box; margin: 0; padding: 0; }
  html, body { width: 1200px; height: 848px; overflow: hidden; background: var(--page); }
  .sheet { position: relative; width: 1200px; height: 848px; background: var(--page); }

  .lounge-photo {
    position: absolute; left: 49px; top: 49px; width: 737px; height: 493px;
    background: linear-gradient(160deg, var(--photo-mid) 0%, var(--photo-light) 38%, var(--photo-mid) 62%, var(--photo-dark) 100%);
  }

  .service-band {
    position: absolute; left: 49px; top: 542px; width: 737px; height: 253px;
    background: var(--sky); color: var(--ink);
    display: grid; grid-template-columns: 1fr 1fr; column-gap: 24px;
    padding: 0 16px 0 11px;
  }
  .offer-column {
    position: absolute; left: 794px; top: 49px; width: 352px; height: 746px;
    background: var(--leaf); color: var(--paper-text);
    padding: 12px 10px 0 16px;
  }

  .feature-title {
    font-family: "Archivo Black", "Arial Black", sans-serif;
    font-size: 16.5px; font-weight: 400; letter-spacing: 0.2px;
    text-align: center; line-height: 1.2;
  }
  .feature-copy {
    font-family: "Arimo", Arial, sans-serif;
    font-size: 14.6px; line-height: 1.3; hyphens: auto;
  }
  .service-band .feature-title { color: var(--paper-text); margin-top: 10px; margin-bottom: 19px; }
  .service-band .feature-copy { font-size: 15.2px; line-height: 1.35; }

  .offer-column .feature { margin-bottom: 48px; }
  .offer-column .feature:nth-child(2) { margin-bottom: 50px; }
</style>
</head>
<body>
<main class="sheet">
  <div class="lounge-photo" role="img" aria-label="Photograph of a modern office break lounge with snack, drink and coffee vending machines, leather sofas and staff taking a break"></div>

  <section class="service-band">
    <article class="feature">
      <h2 class="feature-title">24 hour support</h2>
      <p class="feature-copy">Qorvel Vending solutions is on hand 24 hours a day to provide ongoing support should the unlikely event of a coin jam or maintenance issue arise. Our qualified technicians are on call and will immediately respond to any call outs absolutely free of charge. All our machines are regularly tested and serviced to ensure ongoing reliability and seamless operation.</p>
    </article>
    <article class="feature">
      <h2 class="feature-title">Regular stocking and servicing</h2>
      <p class="feature-copy">Qorvel Vending provides trained technicians to regularly service and restock machines ensuring they are always stocked with the latest products. They will closely monitor your selections and suggest new products based on current sales keeping our service extremely personalized and providing great product variety.</p>
    </article>
  </section>

  <section class="offer-column">
    <article class="feature">
      <h2 class="feature-title">Customized Vending Solutions</h2>
      <p class="feature-copy">Qorvel tailor a unique vending solution for each of our clients either large or small. Clients are able to choose their own range from our large product inventory or even request new items at any time, or alternatively we can design a vending machine product package that will best suit your demographic. We continually strive to improve our service and understand that one size does not fit all. We know different products meet the requirements of different people even at different times and this is why we continually monitor your selections and adjust stock to your needs.</p>
    </article>
    <article class="feature">
      <h2 class="feature-title">A large range of Quality products</h2>
      <p class="feature-copy">Qorvel Vending solutions stock an extremely large range of high quality products that are tailored to individual needs. We have numerous existing clients including industrial centres, offices, shops, schools/training centres, gyms and even health clubs. Such a varied customer base requires a diverse and extensive range of products to choose from. We work with our clients to ensure products are suitable and consistently up to date.</p>
    </article>
    <article class="feature">
      <h2 class="feature-title">Healthier options</h2>
      <p class="feature-copy">We understand the importance of a balanced diet and are committed to providing healthier options. With some of our clients being a health club and gyms we stock a large range of healthy drinks and snacks including gluten free options. We always look for new products that offer superior quality and great pricing to ensure our product range is always up to date and the best available.</p>
    </article>
  </section>
</main>
</body>
</html>
```